Voltara Solutions Ltd - Project for new electric vehicle charging company

Please use Voltara Solutions Ltd logo & artwork instead of Brightwell.

We would like to produce a leaflet to advertise our electric vehicle charging company to build a reputation and workflow in the local area.

We would like to use the attached logo and maintain the colour palette of the of the logo to be simple, modern and effective.

I have over 15 years experience in the electrical industry and have direct access to the latest technology in electric vehicle charging.

All quotes to remain fixed costs subject to survey of the property and maintenance options can be available.

We can also offer further remedial works to any property through our sister company Brightwell Solutions Ltd.

Target Market(s)

Domestic / commercial customers

Requirements
Must have
• Voltara Solutions Ltd logo and colour palette.
Should not have
• Brightwell logo, Email or website address.

```html
<!DOCTYPE html>
<html lang="en">
<head>
<meta charset="utf-8">
<title>Voltara Solutions Ltd – EV Charging Leaflet</title>
<link href="https://fonts.googleapis.com/css2?family=Anton&family=Bebas+Neue&family=Montserrat:ital,wght@0,400;0,500;1,800&family=Oswald:wght@500&display=swap" rel="stylesheet">
<style>
  :root {
    --page-bg: #ffffff;
    --sky-top: #dfe5e8;
    --sky-bottom: #c9d2d6;
    --charcoal: #2b2b2c;
    --teal: #1fbfa5;
    --teal-dark: #0e7f6f;
    --green: #3cb54a;
    --white: #ffffff;
    --grey-icon: #8c8c8c;
    --ink: #111111;
    --star: #f5d232;
  }
  * { box-sizing: border-box; margin: 0; padding: 0; }
  html, body { width: 1200px; height: 2269px; overflow: hidden; background: var(--page-bg); }
  .leaflet {
    position: absolute; left: 40px; top: 410px;
    width: 1120px; height: 1448px; overflow: hidden;
    background: var(--charcoal);
    box-shadow: 0 10px 30px rgba(0,0,0,.25);
    font-family: "Montserrat", Arial, sans-serif;
  }
  .hero {
    position: absolute; left: 0; top: 0; width: 1120px; height: 544px;
    background: linear-gradient(180deg, var(--sky-top), var(--sky-bottom));
  }
  .hero-photo {
    position: absolute; left: 600px; top: 35px; width: 520px; height: 500px;
    background: radial-gradient(ellipse at 55% 55%, #ffffff 0%, #eef1f2 45%, #c3cbcf 100%);
    border-radius: 40% 0 0 30%;
  }
  .headline { position: absolute; left: 70px; top: 112px; }
  .headline-lead {
    display: block; font-family: "Bebas Neue", sans-serif;
    font-size: 96px; line-height: 92px; color: var(--teal); letter-spacing: 1px;
  }
  .headline-main {
    display: block; font-family: "Anton", sans-serif;
    font-size: 138px; line-height: 122px; letter-spacing: -1px;
    color: var(--ink);
  }
  .headline-main.fade {
    background: linear-gradient(180deg, #0b0b0b 25%, var(--teal-dark) 100%);
    -webkit-background-clip: text; background-clip: text; color: transparent;
  }
  .showcase { position: absolute; left: 16px; top: 475px; width: 690px; height: 460px; }
  .showcase svg { display: block; }
  .experience {
    position: absolute; left: 185px; top: 590px; width: 340px;
    text-align: center; color: var(--white);
    font-style: italic; font-weight: 800; line-height: 1.12;
  }
  .experience .stars { color: var(--star); font-size: 18px; letter-spacing: 4px; font-style: normal; display: block; }
  .experience .small { font-size: 20px; display: block; }
  .experience .big { font-size: 30px; display: block; }
  .experience .big small { font-size: 20px; }
  .pitch {
    position: absolute; left: 722px; top: 606px; width: 368px;
    border-left: 3px solid var(--teal); padding-left: 17px;
  }
  .pitch-title {
    color: var(--teal); font-style: italic; font-weight: 800;
    font-size: 26px; line-height: 37px; letter-spacing: -0.3px; text-transform: uppercase;
  }
  .pitch p { color: var(--white); font-size: 17px; line-height: 22px; margin-top: 14px; }
  .services {
    position: absolute; left: 720px; top: 1018px; width: 340px; list-style: none;
  }
  .services li {
    position: relative; padding-left: 22px; color: var(--white);
    font-size: 13px; line-height: 17px; margin-bottom: 9px;
  }
  .services li::before {
    content: ""; position: absolute; left: 0; top: 4px;
    width: 7px; height: 7px; background: var(--teal);
  }
  .brand {
    position: absolute; left: 66px; top: 1100px;
    display: flex; align-items: center; gap: 16px;
  }
  .brand-dot { width: 60px; height: 60px; border-radius: 50%; background: var(--teal); }
  .brand-name { font-size: 40px; font-weight: 500; color: var(--teal); }
  .call {
    position: absolute; left: 78px; top: 1204px; height: 53px;
    display: flex; align-items: stretch;
  }
  .call-icon {
    width: 53px; background: var(--grey-icon); border-radius: 8px 0 0 8px;
    display: flex; align-items: center; justify-content: center;
  }
  .call-label {
    background: var(--teal); color: var(--white);
    font-family: "Bebas Neue", sans-serif; font-size: 38px;
    padding: 8px 34px 0 22px; border-radius: 0 26px 26px 0;
  }
  .call-note {
    position: absolute; left: 78px; top: 1275px; width: 470px;
    color: var(--teal); font-size: 16px; line-height: 21px;
  }
  .footer-band {
    position: absolute; left: 0; top: 1355px; width: 1120px; height: 93px;
    background: var(--green); color: var(--white);
    font-family: "Oswald", sans-serif; font-weight: 500;
    font-size: 20px; line-height: 28px; text-align: center; text-transform: uppercase;
    padding: 18px 90px 0;
  }
</style>
</head>
<body>
<main class="leaflet">
  <section class="hero">
    <div class="hero-photo" role="img" aria-label="Photo of a white electric car plugged into a green charging post"></div>
    <h1 class="headline">
      <span class="headline-lead">Electric Vehicle</span>
      <span class="headline-main">CHARGING</span>
      <span class="headline-main fade">EXPERTS</span>
    </h1>
  </section>

  <div class="showcase">
    <svg width="690" height="460" viewBox="0 0 690 460">
      <defs>
        <linearGradient id="house-tone" x1="0" y1="0" x2="1" y2="1">
          <stop offset="0" stop-color="#2fd6bb"/>
          <stop offset="0.6" stop-color="#17a891"/>
          <stop offset="1" stop-color="#0c6d60"/>
        </linearGradient>
      </defs>
      <path role="img" aria-label="Photo of a modern house with a car charging on the driveway"
            d="M0 300 A345 300 0 0 1 690 300 L690 420 Q520 470 300 440 Q120 420 0 430 Z"
            fill="url(#house-tone)"/>
      <path d="M170 230 Q180 150 345 140 Q520 140 520 240 Q520 300 345 300 Q190 300 170 230 Z"
            fill="var(--charcoal)"/>
    </svg>
  </div>

  <div class="experience">
    <span class="stars">★★★</span>
    <span class="small">WITH OVER</span>
    <span class="big">15 YEARS <small>OF</small></span>
    <span class="small">EXPERIENCE IN THE</span>
    <span class="small">ELECTRICAL INDUSTRY</span>
  </div>

  <section class="pitch">
    <h2 class="pitch-title">Looking for reliable and efficient electric vehicle charging solutions in the local area?</h2>
    <p>Look no further than Voltara Solutions Ltd!</p>
    <p>We have the knowledge and expertise to provide the latest technology in electric vehicle charging.</p>
  </section>

  <ul class="services">
    <li>Installation of electric vehicle charging stations at commercial or residential properties.</li>
    <li>Maintenance and repair services for existing electric vehicle charging stations.</li>
    <li>Consulting services to help businesses and property owners determine the best type and location of charging stations for their needs.</li>
    <li>Design and planning services to ensure that charging stations are installed in compliance with local regulations and codes.</li>
    <li>Integration of electric vehicle charging stations with existing energy management systems or solar power systems.</li>
    <li>Customized charging solutions, such as workplace charging programs, fleet charging, or shared-use charging programs.</li>
  </ul>

  <div class="brand">
    <span class="brand-dot"></span>
    <span class="brand-name">Voltara Solutions Ltd</span>
  </div>

  <div class="call">
    <span class="call-icon">
      <svg width="30" height="30" viewBox="0 0 24 24" aria-hidden="true">
        <path fill="#ffffff" d="M6.6 10.8a15.1 15.1 0 0 0 6.6 6.6l2.2-2.2a1 1 0 0 1 1-.25 11.4 11.4 0 0 0 3.6.57 1 1 0 0 1 1 1V20a1 1 0 0 1-1 1A17 17 0 0 1 3 4a1 1 0 0 1 1-1h3.5a1 1 0 0 1 1 1c0 1.25.2 2.45.57 3.6a1 1 0 0 1-.25 1z"/>
      </svg>
    </span>
    <span class="call-label">CALL US TODAY</span>
  </div>
  <p class="call-note">Call us today to schedule a survey of your property and receive a fixed cost quote. We also offer maintenance options to keep your charging station running smoothly.</p>

  <footer class="footer-band">
    For any additional electrical needs, be sure to check out our sister company Brightwell Solutions Ltd. But for all your electric vehicle charging needs, trust Voltara Solutions Ltd.
  </footer>
</main>
</body>
</html>
```